Kellwood Build, Carpentry Services

Business card for carpentry business in the Sunshine Coast.

Business card layout required using logo provided - provided both PDF copy and AI. Please let me know if you would like a the files for the logo symbol and text by itself.

Business Colours are grey, blue and white. The font colours codes for this design are Blue Hex # 00B4E6 and Hex # 39393B for the gray colour.

FYI font for logo is Gotham Bold.

Preference for a clean and striking layout that is simple and elegant.

Target Market(s)

Young Families, retirees, young couples requiring assistance with small to medium works/renovations on the Sunshine Coast.

Industry/Entity Type

Construction

Contact Information for Business Card

Dean Kellwood
Carpenter
0489305627
dean@kellwoodbuild.com.au
Wattlecove, Seabreeze Coast
RHPA Licensed Carpenter (In smaller font)

Font styles to use
Sans Serif

Colors

Designer to choose colors to be used in the design.

Requirements
Must have
• Logo provided must appear on the card, preferably on one side of the card by itself with the text on the alternate side
Nice to have
• Text on the other side of card, maybe grey background and white font here but happy for the designer to provide ideas here.
Should not have
• Use of other colours, other than the ones provided - white, grey and blue. Black optional.

```html
<!DOCTYPE html>
<html lang="en">
<head>
<meta charset="utf-8">
<title>Kellwood Build – Business Card</title>
<link href="https://fonts.googleapis.com/css2?family=Montserrat:wght@400;500;700&display=swap" rel="stylesheet">
<style>
  :root {
    --blue: #00B4E6;
    --grey: #39393B;
    --card-dark: #434345;
    --white: #FFFFFF;
    --stage: #E9E7E3;
  }
  * { margin: 0; padding: 0; box-sizing: border-box; }
  html, body { width: 900px; height: 1200px; overflow: hidden; }
  body {
    position: relative;
    background: var(--stage);
    font-family: "Montserrat", Arial, sans-serif;
    color: var(--grey);
  }
  .card {
    position: absolute;
    left: 86px;
    width: 736px;
    height: 430px;
    box-shadow: 0 6px 18px rgba(0,0,0,0.25);
  }
  .card--front { top: 137px; background: var(--white); }
  .card--back  { top: 632px; background: var(--card-dark); }

  .brand {
    position: absolute;
    display: flex;
    align-items: center;
    gap: 14px;
    font-weight: 700;
    color: var(--blue);
    letter-spacing: 0.5px;
    white-space: nowrap;
    line-height: 1;
  }
  .brand__mark { background: var(--blue); flex: none; }
  .card--front .brand { right: 52px; top: 71px; font-size: 28px; }
  .card--front .brand__mark { width: 38px; height: 38px; }
  .card--back .brand { left: 50%; top: 183px; transform: translateX(-50%); font-size: 46px; gap: 22px; }
  .card--back .brand__mark { width: 62px; height: 62px; }

  .holder { position: absolute; left: 52px; top: 214px; }
  .holder__name { font-size: 31px; font-weight: 700; color: var(--blue); line-height: 1; letter-spacing: -0.3px; white-space: nowrap; }
  .holder__role { margin-top: 6px; font-size: 18px; font-weight: 500; line-height: 1.2; }

  .contact { position: absolute; left: 52px; top: 300px; list-style: none; }
  .contact__item {
    display: flex; align-items: center; gap: 12px;
    height: 28.5px; font-size: 17px; font-weight: 500; letter-spacing: 0.3px;
    white-space: nowrap;
  }
  .contact__icon { width: 14px; height: 14px; flex: none; }

  .licence {
    position: absolute; right: 53px; top: 357px;
    font-size: 17px; font-weight: 500; letter-spacing: 0.2px;
    line-height: 28.5px; white-space: nowrap;
  }

  .back-email {
    position: absolute; left: 0; right: 0; top: 364px;
    text-align: center; font-size: 17px; font-weight: 500;
    color: var(--white); letter-spacing: 0.3px;
  }
  .back-email__domain { color: var(--blue); }
</style>
</head>
<body>

  <section class="card card--front">
    <div class="brand"><span class="brand__mark"></span>KELLWOOD BUILD</div>

    <div class="holder">
      <h1 class="holder__name">DEAN KELLWOOD</h1>
      <p class="holder__role">Carpenter</p>
    </div>

    <ul class="contact">
      <li class="contact__item">
        <svg class="contact__icon" viewBox="0 0 24 24" aria-hidden="true"><path fill="#00B4E6" d="M6.6 10.8a15.2 15.2 0 0 0 6.6 6.6l2.2-2.2a1 1 0 0 1 1-.25 11.4 11.4 0 0 0 3.6.57 1 1 0 0 1 1 1V20a1 1 0 0 1-1 1A17 17 0 0 1 3 4a1 1 0 0 1 1-1h3.5a1 1 0 0 1 1 1c0 1.250.2 2.46.57 3.6a1 1 0 0 1-.25 1z"/></svg>
        0489305627
      </li>
      <li class="contact__item">
        <svg class="contact__icon" viewBox="0 0 24 24" aria-hidden="true"><path fill="#00B4E6" d="M2 5h20v14H2z"/><path fill="none" stroke="#fff" stroke-width="2" d="M2 6l10 7 10-7"/></svg>
        dean@kellwoodbuild.com.au
      </li>
      <li class="contact__item">
        <svg class="contact__icon" viewBox="0 0 24 24" aria-hidden="true"><path fill="none" stroke="#00B4E6" stroke-width="2" d="M12 22s-7-7.5-7-13a7 7 0 0 1 14 0c0 5.5-7 13-7 13z"/><circle cx="12" cy="9" r="2.5" fill="none" stroke="#00B4E6" stroke-width="2"/></svg>
        Wattlecove, Seabreeze Coast
      </li>
    </ul>

    <p class="licence">RHPA Licensed Carpenter</p>
  </section>

  <section class="card card--back">
    <div class="brand"><span class="brand__mark"></span>KELLWOOD BUILD</div>
    <p class="back-email">dean@<span class="back-email__domain">kellwoodbuild</span>.com.au</p>
  </section>

</body>
</html>
```